Renewable Energy Consultancy needs relatively simple but smart website

We are a renewable energy focussed consultancy called Bellmoran, and we are just starting out. Our target is to bring knowledge of the detailed technical and commercial operations of renewables projects, mainly wind energy.

Our target customers are major energy utilities and private finance groups, who look to invest in renewables projects as a long term money-earning system. We are a fairly young, dynamic team of industry-respected people (4 of us) but we need to make ourselves look bigger than this (our customers will expect us to take on major projects, so we need to look big enough to handle it...)

We're not going to sell anything from our website and we expect it to just support our company name. Most of our customers are made by strong networks and relationships, so its mainly there to give confidence in our capabilities and give a strong view of who we are. We probably need a site with 4/5 pages which we can then expand when needed.

We have logos and headers (attached) which we want to use (also run through artpitchly), and I've attached a few pictures of projects similar to those we will be involved in to give us a feel for how it will look. Also attached are the colours we liked which are now used in the logo, and the font details. Whilst we're a "green" company with a "green" logo, we don't want to be completely green, so some nice combinations of colours on the pages would be good.

Ideally we need to have chirpnet/workgrid news feeds somewhere linked into the site.

The design should be smart - giving a feel of high integrity and assurance whilst making us seem approachable and knowledgeable.

Target Market(s)

Renewables investors, developers of renewables projects (wind farms etc),

Industry/Entity Type

Finance

Coding

Coded - Design and coding required

Number of Pages Required

4 page

Other font styles liked:
• See the attachment with brand text/colour details ("colour codes" filename)

Requirements
Must have
• A fairly simple, but smart website design. We're looking to provide confidence and consolidate our networks with the website, not specifically find new customers - so its really just to give customers somewhere they can relate to online
Nice to have
• We have logos/brands and colours - so a website which incorperates these well and brings accross a professional company
• Would be nice to have a page (such as a blog/wordpress) we can easily update with news/events etc and links to chirpnet feed and workgrid feed ideally.
Should not have
• cartoons, flashy gimmicks,

```html
<!DOCTYPE html>
<html lang="en">
<head>
<meta charset="utf-8">
<title>Bellmoran – Renewable Energy Consultancy</title>
<link rel="stylesheet" href="https://fonts.googleapis.com/css2?family=Jost:wght@300;400;500&display=swap">
<style>
  :root {
    --brand-green: #6aa50d;
    --brand-green-dark: #3f7a06;
    --footer-green: #1f4d05;
    --ink: #1c1c1c;
    --body-grey: #6b6b6b;
    --logo-grey: #6e6e6e;
    --button-dark: #3a3a3c;
    --frame: #dcdcdc;
    --white: #ffffff;
  }
  * { margin: 0; padding: 0; box-sizing: border-box; }
  html, body { width: 986px; height: 1200px; overflow: hidden; background: var(--white); }
  body { position: relative; font-family: Arial, Helvetica, sans-serif; color: var(--ink); }
  .abs { position: absolute; }

  .top-bar { left: 0; top: 0; width: 986px; height: 4px; background: var(--brand-green); }
  .top-bar-notch { left: 436px; top: 4px; width: 0; height: 0; border-left: 8px solid transparent; border-right: 8px solid transparent; border-top: 8px solid var(--brand-green); }

  .brand { left: 90px; top: 20px; }
  .brand-name { font-family: 'Jost', sans-serif; font-weight: 300; font-size: 33px; color: var(--logo-grey); letter-spacing: 1px; line-height: 38px; }

  .main-nav a { position: absolute; top: 37px; font-size: 11.5px; color: var(--ink); text-decoration: none; white-space: nowrap; }

  .hero { left: 90px; top: 75px; width: 806px; height: 388px;
    background: linear-gradient(100deg, #c9d0e2 0%, #d7dbe8 35%, #9da2ad 55%, #8a3a34 75%, #d8dde6 100%); }
  .hero-title { left: 113px; top: 152px; font-family: 'Jost', sans-serif; font-weight: 400; font-size: 33px; color: var(--ink); white-space: nowrap; }
  .hero-text { left: 115px; top: 202px; width: 330px; font-family: 'Jost', sans-serif; font-weight: 300; font-size: 15px; line-height: 18.5px; color: #2a2a2a; }
  .hero-btn { left: 113px; top: 291px; width: 86px; height: 28px; background: var(--button-dark); color: var(--white); font-family: 'Jost', sans-serif; font-size: 10.5px; letter-spacing: .5px; line-height: 28px; text-align: center; }

  .feature { top: 499px; }
  .feature-head { display: flex; align-items: center; gap: 15px; height: 36px; }
  .feature-icon { width: 34px; height: 34px; flex: none; }
  .feature-title { font-family: 'Jost', sans-serif; font-weight: 400; font-size: 22px; color: var(--ink); white-space: nowrap; }
  .feature-text { margin-top: 12px; font-size: 11.5px; line-height: 16.5px; color: var(--body-grey); }
  .btn-dark { display: inline-block; margin-top: 10px; height: 28px; padding: 0 7px; background: var(--button-dark); color: var(--white); font-family: 'Jost', sans-serif; font-weight: 500; font-size: 11.5px; line-height: 28px; }

  .divider { left: 93px; top: 661px; width: 803px; border-top: 1px dotted #bdbdbd; }

  .section-title { left: 94px; top: 686px; font-family: 'Jost', sans-serif; font-size: 21px; font-weight: 400; color: var(--ink); }

  .service { top: 729px; width: 194px; }
  .service-frame { width: 194px; height: 111px; border: 1px solid var(--frame); padding: 4px; }
  .service-photo { width: 100%; height: 100%; }
  .service-caption { margin-top: 17px; font-family: 'Jost', sans-serif; font-weight: 400; font-size: 13px; line-height: 15px; color: var(--ink); }

  .site-footer { left: 0; top: 917px; width: 986px; height: 242px; background: var(--footer-green); color: var(--white); font-family: 'Jost', sans-serif; }
  .footer-heading { position: absolute; top: 22px; font-size: 12.5px; font-weight: 400; letter-spacing: .2px; }
  .topic-list { position: absolute; left: 91px; top: 55px; list-style: none; font-size: 11.5px; line-height: 23px; }
  .blog-item { position: absolute; left: 218px; width: 195px; font-size: 10px; line-height: 12.5px; }
  .blog-thumb { float: left; width: 37px; height: 35px; margin-right: 8px; }
  .blog-date { font-style: italic; font-size: 8.5px; margin-top: 2px; }
  .blog-rule { font-size: 9px; line-height: 12px; }
  .map { position: absolute; left: 464px; top: 55px; width: 176px; height: 72px; background: linear-gradient(135deg, #e9e4c7, #d7cfa4 50%, #a8c0d8); }
  .contact-lines { position: absolute; left: 466px; top: 139px; font-size: 10.5px; line-height: 19px; }
  .news-text { position: absolute; left: 694px; top: 53px; width: 190px; font-size: 10px; line-height: 12.5px; }
  .signup { position: absolute; left: 694px; top: 86px; display: flex; }
  .signup-input { width: 149px; height: 30px; background: var(--white); color: #8a8a8a; font-style: italic; font-size: 11px; line-height: 30px; padding-left: 7px; }
  .signup-btn { width: 54px; height: 30px; background: #1a1a1a; color: var(--white); font-size: 11.5px; line-height: 30px; text-align: center; }
  .social { position: absolute; left: 695px; top: 135px; display: flex; gap: 10px; font-size: 10px; line-height: 12px; }
  .social span { display: flex; align-items: center; gap: 4px; }
  .social i { width: 9px; height: 9px; background: var(--white); display: inline-block; }

  .copyright { left: 90px; top: 1172px; font-family: 'Jost', sans-serif; font-size: 11px; color: var(--ink); }
  .legal { left: 754px; top: 1172px; font-family: 'Jost', sans-serif; font-size: 11px; color: var(--ink); white-space: nowrap; }
  .legal b { font-weight: 400; margin: 0 8px; }
</style>
</head>
<body>
  <div class="abs top-bar"></div>
  <div class="abs top-bar-notch"></div>

  <header>
    <div class="abs brand"><span class="brand-name">Bellmoran</span></div>
    <nav class="main-nav">
      <a style="left:427px">Home</a>
      <a style="left:492px">Services</a>
      <a style="left:571px">Filed Personel</a>
      <a style="left:681px">Projects</a>
      <a style="left:757px">About Us</a>
      <a style="left:839px">Contact Us</a>
    </nav>
  </header>

  <div class="abs hero" role="img" aria-label="Photo of an offshore wind installation vessel loaded with turbine blades and towers at a harbour"></div>
  <h1 class="abs hero-title">Welcome To Bellmoran</h1>
  <p class="abs hero-text">Lorem ipsum dolor sit amet, consectetur adip iscing elit, sed do eiusmod tempor.Lorem ipsum dolor sit amet, consectetur adip iscing elit, sed do eiusmod tempor.</p>
  <div class="abs hero-btn">READ MORE</div>

  <section class="abs feature" style="left:91px;width:263px">
    <div class="feature-head">
      <svg class="feature-icon" viewBox="0 0 34 34"><rect x="2" y="2" width="30" height="30" rx="6" fill="var(--brand-green)"/><path d="M11 17h12M17 11v12" stroke="#fff" stroke-width="2.4"/></svg>
      <h2 class="feature-title">Welcome To Bellmoran</h2>
    </div>
    <p class="feature-text">Lorem ipsum dolor sit amet, consectetur adip iscing elit, sed do eiusmod tempor incididuntut labore et dolore magna aliqua.</p>
    <span class="btn-dark">Read More</span>
  </section>
  <section class="abs feature" style="left:396px;width:232px">
    <div class="feature-head">
      <svg class="feature-icon" viewBox="0 0 34 34"><circle cx="17" cy="17" r="17" fill="var(--brand-green)"/><rect x="10" y="10" width="14" height="14" rx="2" fill="none" stroke="#fff" stroke-width="2"/><path d="M13 17l3 3 6-7" fill="none" stroke="#fff" stroke-width="2.2"/></svg>
      <h2 class="feature-title">Why Choose Us?</h2>
    </div>
    <p class="feature-text">Lorem ipsum dolor sit amet, consectetur adip iscing elit, sed do eiusmod tempor incididunt ut labore et dolore magna aliqua.</p>
    <span class="btn-dark">Read More</span>
  </section>
  <section class="abs feature" style="left:668px;width:232px">
    <div class="feature-head">
      <svg class="feature-icon" viewBox="0 0 34 34"><circle cx="17" cy="17" r="17" fill="var(--brand-green)"/><path d="M8 15h7l-2-5 4 0 8 7-8 7-4 0 2-5H8z" fill="#fff"/></svg>
      <h2 class="feature-title">Quality Policy</h2>
    </div>
    <p class="feature-text">Lorem ipsum dolor sit amet, consectetur adip iscing elit, sed do eiusmod tempor incididunt ut labore et dolore magna aliqua.</p>
    <span class="btn-dark">Read More</span>
  </section>

  <div class="abs divider"></div>
  <h2 class="abs section-title">Our Sevices</h2>

  <div class="abs service" style="left:90px">
    <div class="service-frame"><div class="service-photo" role="img" aria-label="Aerial photo of a turbine being installed at sea" style="background:linear-gradient(180deg,#5c7282,#3e5665)"></div></div>
    <p class="service-caption">Lorem ipsum dolor sit amet, consectetur adip.</p>
  </div>
  <div class="abs service" style="left:294px">
    <div class="service-frame"><div class="service-photo" role="img" aria-label="Photo of turbine blades stacked on a vessel deck at dusk" style="background:linear-gradient(135deg,#8f98a4,#4a4e55 60%,#2a2624)"></div></div>
    <p class="service-caption">Lorem ipsum dolor sit amet, consectetur adip.</p>
  </div>
  <div class="abs service" style="left:498px">
    <div class="service-frame"><div class="service-photo" role="img" aria-label="Aerial photo of an offshore wind turbine in open sea" style="background:linear-gradient(180deg,#2f5f96,#23508a)"></div></div>
    <p class="service-caption">Lorem ipsum dolor sit amet, consectetur adip.</p>
  </div>
  <div class="abs service" style="left:702px">
    <div class="service-frame"><div class="service-photo" role="img" aria-label="Photo of onshore wind turbines over farmland" style="background:linear-gradient(180deg,#a9c6e6,#d6e4f0 75%,#6b7a4a)"></div></div>
    <p class="service-caption">Lorem ipsum dolor sit amet, consectetur adip.</p>
  </div>

  <footer class="abs site-footer">
    <h3 class="footer-heading" style="left:90px">TOPIC</h3>
    <ul class="topic-list">
      <li>Home</li><li>Services</li><li>About Us</li><li>Projects</li><li>Wind Farm</li><li>Contact Us</li>
    </ul>

    <h3 class="footer-heading" style="left:218px">OUR BLOG</h3>
    <div class="blog-item" style="top:52px">
      <div class="blog-thumb" role="img" aria-label="Thumbnail of a wind installation vessel" style="background:linear-gradient(135deg,#aab4c4,#6a4a48)"></div>
      <p>Lorem ipsum dolor sit amet, consectetur adip iscing elit, sed do eiusmod tempor</p>
      <p>Lorem ipsum dolor sit amet, consect etur.</p>
      <p class="blog-date">Mar 16, 2015</p>
      <p class="blog-rule">-------------------------</p>
    </div>
    <div class="blog-item" style="top:133px">
      <div class="blog-thumb" role="img" aria-label="Thumbnail of wind turbines against a blue sky" style="background:linear-gradient(180deg,#9fbfe0,#e4edf5)"></div>
      <p>Lorem ipsum dolor sit amet, consectetur adip iscing elit, sed do eiusmod tempor</p>
      <p>Lorem ipsum dolor sit amet, consect etur.</p>
      <p class="blog-date">Mar 16, 2015</p>
      <p class="blog-rule">-------------------------</p>
    </div>

    <h3 class="footer-heading" style="left:464px">LOCATION AND CONTACT</h3>
    <div class="map" role="img" aria-label="Street map of the office location"></div>
    <div class="contact-lines">
      <p>Address: Lorem Ipsum dolor sit, AMET</p>
      <p>Email: hello@bellmoran.com</p>
      <p>Phone: +000-555-0147</p>
      <p class="blog-rule">-------------------------</p>
    </div>

    <h3 class="footer-heading" style="left:693px">SIGN UP FOR NEWSLETTER</h3>
    <p class="news-text">Lorem ipsum dolor sit amet, consectetur adip iscing elit,</p>
    <div class="signup"><div class="signup-input">enter email address</div><div class="signup-btn">Sign up</div></div>
    <div class="social">
      <span><i></i>friendbook</span>
      <span><i></i>chirpnet</span>
      <span><i></i>workgrid</span>
      <span><i></i>RSS</span>
    </div>
  </footer>

  <p class="abs copyright">Copyright 2013 Bellmoran. All Rights Reserved.</p>
  <p class="abs legal">Privacy<b>|</b>Terms &amp; Conditions</p>
</body>
</html>
```